Webdesign für Kreislauf- und Handelsberatung
Zielgruppe
- Kreislauf- und Handelsberatung
- Erarbeitung von Konzepten und Lösungen für Recyclingunternehmen
Aufgabenstellung
keine Googlemaps-Karte in das Mockup
Navigation:
- Home
- Leistungen
- Beratung
- Vertrieb
- Recycling
- Zertifikate
- Vorstellung
- Partner
- Aktuelles
- Kontakt
- Impressum / Datenschutz
in den content vorrangig die Leistungen und den Kontakt darstellen
NUR FOTOS VON 'PIXANTO' NUTZEN!

```html
<!DOCTYPE html>
<html lang="de">
<head>
<meta charset="utf-8">
<title>Grünkreis – Kreislauf- und Handelsberatung</title>
<link rel="stylesheet" href="https://fonts.googleapis.com/css2?family=Poppins:wght@600;700&family=Jost:wght@400;500&display=swap">
<style>
  :root{
    --green:#7cb342;
    --text-dark:#4d4d4d;
    --white:#ffffff;
    --black:#000000;
    --footer:#e1e1e1;
    --outline:#555555;
  }
  *{box-sizing:border-box;margin:0;padding:0}
  html,body{width:1200px;height:662px;overflow:hidden;background:var(--white)}
  body{font-family:"Jost",Arial,sans-serif;color:var(--text-dark);position:relative}

  .site-header{position:absolute;left:0;top:0;width:1200px;height:163px}
  .brand-name{position:absolute;left:0;width:1200px;top:18px;text-align:center;font-family:"Poppins",sans-serif;font-weight:700;font-size:46px;line-height:56px;color:var(--green)}
  .brand-rule{position:absolute;left:410px;top:77px;width:401px;height:2px;background:var(--green)}
  .brand-tagline{position:absolute;left:0;width:1200px;top:89px;text-align:center;font-family:"Poppins",sans-serif;font-weight:600;font-size:23px;line-height:32px;color:var(--text-dark)}

  .main-nav{position:absolute;top:132px;left:0;width:1200px;height:17px}
  .main-nav a{position:absolute;top:0;height:17px;border:1px solid var(--outline);border-radius:9px;font-size:10px;line-height:15px;text-align:center;text-decoration:none;color:var(--text-dark);letter-spacing:.3px}
  .main-nav a.is-active{background:var(--green);border-color:var(--green)}

  .hero{position:absolute;top:163px;left:0;width:1200px;height:363px}
  .hero-visual{position:absolute;left:0;top:0;width:723px;height:363px;
    background:radial-gradient(ellipse at 50% 45%,#8fcf3e 0%,#7fbb3a 22%,#b9c7a6 45%,#c9cdc9 70%,#a9aca8 100%)}
  .hero-panel{position:absolute;left:723px;top:0;width:477px;height:363px;background:var(--green);color:var(--white)}
  .hero-title{position:absolute;left:56px;top:66px;width:340px;font-family:"Poppins",sans-serif;font-weight:700;font-size:24px;line-height:35px}
  .hero-list{position:absolute;left:56px;top:196px;width:322px;font-size:8.6px;line-height:11.4px;padding-left:12px}

  .contact-band{position:absolute;top:526px;left:0;width:1200px;height:82px;display:flex}
  .contact-item{height:82px;display:flex;align-items:center;justify-content:center;gap:16px;font-size:9px;font-weight:500;line-height:12px}
  .contact-cta{width:398px;background:var(--green);color:var(--white)}
  .contact-cta span{text-align:center}
  .contact-mail{width:405px;background:var(--white);color:var(--text-dark);font-size:10px;font-weight:400;letter-spacing:.4px}
  .contact-phone{width:397px;background:var(--black);color:var(--white);text-align:center}

  .site-footer{position:absolute;top:608px;left:0;width:1200px;height:54px;background:var(--footer)}
  .copyright{position:absolute;left:24px;top:22px;font-size:7px;color:var(--text-dark)}
  .footer-links a{position:absolute;top:19px;height:17px;border:1px solid var(--outline);border-radius:9px;font-size:9px;line-height:15px;text-align:center;text-decoration:none;color:var(--text-dark)}
</style>
</head>
<body>
  <header class="site-header">
    <div class="brand-name">Grünkreis</div>
    <div class="brand-rule"></div>
    <div class="brand-tagline">Kreislauf- und Handelsberatung</div>
    <nav class="main-nav">
      <a href="#" class="is-active" style="left:112px;width:79px">HOME</a>
      <a href="#" style="left:204px;width:108px">LEISTUNGEN</a>
      <a href="#" style="left:325px;width:100px">BERATUNG</a>
      <a href="#" style="left:438px;width:91px">VERTRIEB</a>
      <a href="#" style="left:543px;width:102px">RECYCLING</a>
      <a href="#" style="left:659px;width:105px">ZERTIFIKATE</a>
      <a href="#" style="left:776px;width:116px">VORSTELLUNG</a>
      <a href="#" style="left:905px;width:90px">PARTNER</a>
      <a href="#" style="left:1008px;width:100px">AKTUELLES</a>
    </nav>
  </header>

  <section class="hero">
    <div class="hero-visual" role="img" aria-label="Foto: Hand hält ein grünes Recycling-Pfeilsymbol vor unscharfem hellem Hintergrund"></div>
    <div class="hero-panel">
      <h1 class="hero-title">Erarbeitung von Konzepten und Lösungen für Recyclingunternehmen</h1>
      <ul class="hero-list">
        <li>Lorem ipsum dolor sit amet, consetetur sadipscing elitr, sed diam nonumy eirmod tempor invidunt ut labore et dolore magna aliquyam erat, sed diam voluptua. At vero eos et accusam et justo duo dolores et ea rebum.</li>
        <li>Stet clita kasd gubergren, no sea takimata sanctus est Lorem ipsum dolor sit amet. Lorem ipsum dolor sit amet, consetetur sadipscing elitr,</li>
        <li>sed diam nonumy eirmod tempor invidunt ut labore et dolore magna aliquyam erat, sed diam voluptua. At vero eos et accusam et</li>
        <li>justo duo dolores et ea rebum. Stet clita kasd gubergren, no sea takimata sanctus est Lorem ipsum dolor sit amet</li>
      </ul>
    </div>
  </section>

  <section class="contact-band">
    <div class="contact-item contact-cta">
      <svg width="30" height="22" viewBox="0 0 30 22" fill="none" stroke="#fff" stroke-width="1.3" aria-hidden="true">
        <circle cx="6" cy="6" r="3"/><circle cx="15" cy="5" r="3"/><circle cx="24" cy="6" r="3"/>
        <path d="M1 20v-6a4 4 0 0 1 4-4h2a4 4 0 0 1 4 4v6"/>
        <path d="M10 20v-7a4 4 0 0 1 4-4h2a4 4 0 0 1 4 4v7"/>
        <path d="M19 20v-6a4 4 0 0 1 4-4h2a4 4 0 0 1 4 4v6"/>
      </svg>
      <span>KONTAKTIEREN SIE UNS FÜR IHRE<br>ERSTBERATUNG</span>
    </div>
    <div class="contact-item contact-mail">
      <svg width="28" height="20" viewBox="0 0 28 20" fill="none" stroke="#111" stroke-width="1.6" aria-hidden="true">
        <rect x="1" y="1" width="26" height="18"/><path d="M1 1l13 10L27 1"/>
      </svg>
      <span>JONAS.BERKHOLZ@GRUENKREIS-MITTELSTADT.DE</span>
    </div>
    <div class="contact-item contact-phone">
      <svg width="22" height="28" viewBox="0 0 22 28" fill="none" stroke="#fff" stroke-width="1.6" aria-hidden="true">
        <path d="M7 2l4 6-3 3c1 4 3 7 6 9l3-3 4 5-3 3C10 24 3 14 3 5z"/>
      </svg>
      <span>TELEFON: +49 XXXXX<br>TELEFAX: +49 XXXX</span>
    </div>
  </section>

  <footer class="site-footer">
    <p class="copyright">© Grünkreis Kreislauf- und Handelsberatung 2019</p>
    <div class="footer-links">
      <a href="#" style="left:916px;width:102px">KONTAKT</a>
      <a href="#" style="left:1031px;width:146px">IMPRESSUM / DATENSCHUTZ</a>
    </div>
  </footer>
</body>
</html>
```